Design our branded business card!

We'd love for you to design our business card and come up with a fitting design that reflects the Pivex brand. We're a growing tech startup with big ambitions. We've included our brand guidelines (contain colour palette), logo (EPS vector in CMYK) and old designs to help you on your way.

We'd like to keep the design fairly simple:

* Name
* Phone number
* Email address
* Website (www.pivex.life)
* Twitter (@pivex)
* Address (18 Wexham Row, Leeds, UK, LS9 4ZQ).

This would need to include print and cutting marks.

If you have any questions just let us know!

Target Market(s)

Businesses, Press and our customers!

Industry/Entity Type

Business

Contact Information for Business Card

* Name
* Phone number
* Email address
* Twitter (@pivex)

Font styles to use
Sans Serif

Requirements
Must have
• 1. Must have the Pivex logo included.
• 2. Must use the font 'Brandon Text' in either 'light' or 'thin' (https://www.typevault-demo.com/fonts/qrsfonts/halden-sans/)
• 3. Must use exact colours references from the brand guidelines. Colours outside of the brand guidelines will be discounted. White (transparent) backgrounds are fine.
• 4. Must contain the following information:
• * Name
• * Phone number
• * Email address
• * Website (www.pivex.life)
• * Twitter (@pivex)
• * Address (18 Wexham Row, Leeds, UK, LS9 4ZQ).
Nice to have
• Must use the font 'Brandon Text' in either 'light' or 'thin' (https://www.typevault-demo.com/fonts/qrsfonts/halden-sans/)
Should not have
• Colours outside of the brand guidelines will be discounted. White (transparent) backgrounds are fine.
• Avoid creating icons or including photography.

```html
<!DOCTYPE html>
<html lang="en">
<head>
<meta charset="utf-8">
<title>Pivex Business Card</title>
<link rel="stylesheet" href="https://fonts.googleapis.com/css2?family=PT+Sans:wght@400;700&display=swap">
<style>
  :root {
    --stage: #3b3430;
    --card: #0c0c0c;
    --brand-green: #7cc671;
    --ink-light: #e6e6e6;
    --logo-silver: #d4d4d4;
    --divider: #2a2a2a;
  }
  html, body {
    margin: 0;
    padding: 0;
    width: 1200px;
    height: 900px;
    overflow: hidden;
    background: var(--stage);
    font-family: "PT Sans", Arial, sans-serif;
  }
  .stage {
    position: relative;
    width: 1200px;
    height: 900px;
  }
  .card {
    position: absolute;
    top: 282px;
    width: 520px;
    height: 336px;
    background: var(--card);
    box-shadow: 0 8px 24px rgba(0,0,0,0.45);
    overflow: hidden;
  }
  .card--front { left: 50px; }
  .card--back { left: 630px; }

  /* Front side */
  .brand-mark {
    position: absolute;
    left: 40px;
    top: 68px;
    width: 200px;
    height: 200px;
  }
  .brand-mark__name {
    position: absolute;
    left: 0;
    right: 0;
    top: 214px;
    text-align: center;
    color: var(--brand-green);
    font-size: 22px;
    font-weight: 400;
    letter-spacing: 1px;
  }
  .divider {
    position: absolute;
    left: 272px;
    top: 62px;
    width: 1px;
    height: 214px;
    background: var(--divider);
  }
  .details {
    position: absolute;
    left: 292px;
    top: 64px;
    color: var(--ink-light);
    font-size: 15px;
    line-height: 21px;
  }
  .details__name {
    color: var(--brand-green);
    font-weight: 700;
    font-size: 18px;
    margin: 0 0 12px;
  }
  .details__address {
    margin: 0 0 12px;
  }
  .contact-list {
    list-style: none;
    margin: 0;
    padding: 0;
  }
  .contact-list li {
    display: flex;
    align-items: center;
    gap: 9px;
    height: 22px;
  }
  .contact-list svg {
    width: 11px;
    height: 11px;
    flex: none;
  }

  /* Back side */
  .back-logo {
    position: absolute;
    left: 0;
    right: 0;
    top: 0;
    bottom: 0;
    display: flex;
    align-items: center;
    justify-content: center;
    gap: 18px;
  }
  .back-logo__dot {
    width: 84px;
    height: 84px;
    border-radius: 50%;
    background: var(--logo-silver);
  }
  .back-logo__name {
    color: var(--logo-silver);
    font-size: 64px;
    font-weight: 400;
    letter-spacing: 2px;
  }
</style>
</head>
<body>
<main class="stage">

  <section class="card card--front" aria-label="Business card front">
    <div class="brand-mark">
      <svg width="200" height="200" viewBox="0 0 200 200" aria-hidden="true">
        <circle cx="100" cy="96" r="96" fill="var(--brand-green)"/>
      </svg>
    </div>
    <div class="divider"></div>
    <div class="details">
      <p class="details__name">Daniel Hartley</p>
      <p class="details__address">18 Wexham Row, Leeds, UK<br>LS9 4ZQ</p>
      <ul class="contact-list">
        <li>
          <svg viewBox="0 0 12 12" aria-hidden="true"><path d="M2.5 1 L4.5 1 L5.3 3.6 L4 4.6 C4.7 6 6 7.3 7.4 8 L8.4 6.7 L11 7.5 L11 9.5 C11 10.4 10.4 11 9.5 11 C5 11 1 7 1 2.5 C1 1.6 1.6 1 2.5 1Z" fill="var(--brand-green)"/></svg>
          <span>044-987 654 321</span>
        </li>
        <li>
          <svg viewBox="0 0 12 12" aria-hidden="true"><rect x="1" y="2.5" width="10" height="7" fill="var(--brand-green)"/><path d="M1 2.8 L6 6.6 L11 2.8" fill="none" stroke="var(--card)" stroke-width="1"/></svg>
          <span>info@pivexmail.com</span>
        </li>
        <li>
          <svg viewBox="0 0 12 12" aria-hidden="true"><circle cx="6" cy="6" r="5" fill="var(--brand-green)"/><path d="M1 6 H11 M6 1 C3.5 3.5 3.5 8.5 6 11 M6 1 C8.5 3.5 8.5 8.5 6 11" fill="none" stroke="var(--card)" stroke-width="0.8"/></svg>
          <span>www.pivex.life</span>
        </li>
        <li>
          <svg viewBox="0 0 12 12" aria-hidden="true"><rect x="1" y="1" width="10" height="10" fill="var(--brand-green)"/></svg>
          <span>@pivex</span>
        </li>
      </ul>
    </div>
  </section>

  <section class="card card--back" aria-label="Business card back">
    <div class="back-logo">
      <div class="back-logo__dot"></div>
      <span class="back-logo__name">pivex</span>
    </div>
  </section>

</main>
</body>
</html>
```